Stylish Business Card for Modern hair salon

I need a simple business card design using our salon logo and colours that are in the logo. We service clients of all ages but predominantly those in the 18 to 55 age range. We have a young staff and are looking to have a card that will present a modern and clean image that represents who we are. The card should be in black and white same as our logo. Minimal use of other colours is allowed.

Industry/Entity Type

Hair And Beauty

Contact Information for Business Card

The design should have the following information
salon name - TR Hair Studio
address - 2751 Birchfield Rd.E. Mississauga, ON L7P3K2
phone - 905 614-2870
website - trhairexample.ca
instagram - tr.hairstudio
twitter - @TR_HairStudio

Colors
000000
ffffff
474747

Requirements
Must have
• simple design, salon name, address, phone, website, instagram, twitter info
• Back of card should have the following:
• YOUR NEXT APPOINTMENT
• DATE
• TIME
Nice to have
• simple design, clear to see and read,
• predominantly black and white colour, minimal use of other colours is ok
Should not have
• many colours, various fonts

```html
<!DOCTYPE html>
<html lang="en">
<head>
<meta charset="utf-8">
<title>TR Hair Studio – Appointment Card</title>
<link rel="stylesheet" href="https://fonts.googleapis.com/css2?family=Bodoni+Moda:opsz,wght@6..96,400&display=swap">
<style>
  :root {
    --ink: #000000;
    --paper: #ffffff;
    --grey: #474747;
  }
  * { margin: 0; padding: 0; box-sizing: border-box; }
  html, body {
    width: 1200px;
    height: 686px;
    overflow: hidden;
    background: var(--paper);
  }
  .card {
    position: relative;
    width: 1200px;
    height: 686px;
    background: var(--paper);
    font-family: "Bodoni Moda", "Didot", serif;
    color: var(--ink);
  }
  .card-frame {
    position: absolute;
    left: 23px;
    top: 23px;
    width: 1154px;
    height: 640px;
    border: 2px solid var(--ink);
  }
  .salon-name {
    position: absolute;
    left: 0;
    top: 150px;
    width: 1200px;
    text-align: center;
    font-size: 100px;
    font-weight: 400;
    line-height: 1;
    letter-spacing: 2px;
    color: var(--ink);
  }
  .appointment-row {
    position: absolute;
    left: 0;
    width: 1200px;
    height: 50px;
  }
  .appointment-row.next { top: 478px; }
  .appointment-row.time { top: 527px; }
  .appointment-label {
    position: absolute;
    right: 586px;
    bottom: 10px;
    font-size: 41px;
    font-weight: 400;
    line-height: 1;
    white-space: nowrap;
    letter-spacing: -0.5px;
  }
  .write-line {
    position: absolute;
    left: 648px;
    width: 413px;
    bottom: 10px;
    height: 0;
    border-top: 1.5px solid var(--ink);
  }
</style>
</head>
<body>
  <main class="card">
    <div class="card-frame"></div>

    <h1 class="salon-name">TR Hair Studio</h1>

    <div class="appointment-row next">
      <span class="appointment-label">Your Next Appointment:</span>
      <span class="write-line"></span>
    </div>
    <div class="appointment-row time">
      <span class="appointment-label">Time:</span>
      <span class="write-line"></span>
    </div>
  </main>
</body>
</html>
```